Revamp Current Website From 2012 TO 2018

We need a ravamp to our current website. I prefer a professional corporate modern feel to it.

My Current Website is www.brightlanepromoworks.biz. Please redesign the homepage and the /certs page first....see attached document for specific instructions..

There is a lot of content at the bottom but maybe we can shorten that by using titles and a pop up of the details or something so it doesnt take too mcuh space...or maybe a red more hyperlink to see the rest of info in pop up or something or new page...

Target Market(s)

B2B, business owners, website owners, marketing companies.

Industry/Entity Type

Promotional Product

Number of Pages Required

2 page

Colors

Designer to choose colors to be used in the design.

Requirements
Must have
• Please keep in mind logo mock up I am working on that looks beautiful on dark background for header...see attached for logo
• Must use existing content I hope your marketing mind comes in to play when designing the website.
• Must have all my content provided on each page...
Nice to have
• similiar color scheme...
Should not have
• I dont like using templates because usually hard to expand on design in future so Prefer full custom designs
• Please no templates

```html
<!DOCTYPE html>
<html lang="en">
<head>
<meta charset="utf-8">
<title>BrightLane Promoworks – Promotional Incentives</title>
<link rel="stylesheet" href="https://fonts.googleapis.com/css2?family=Raleway:wght@600;700;800&family=Open+Sans:wght@400;600;700&display=swap">
<style>
:root{
  --blue:#1679c6;
  --blue-dark:#0f5e9e;
  --ink:#1c2026;
  --ink-2:#262b33;
  --text:#4a4f57;
  --muted:#7b818a;
  --line:#dfe3e8;
  --pale:#f1f3f5;
  --white:#ffffff;
}
*{box-sizing:border-box;margin:0;padding:0}
html,body{width:1200px;height:5202px;overflow:hidden}
body{font-family:"Open Sans",Arial,sans-serif;color:var(--text);background:var(--white);font-size:13px;line-height:1.6}
h1,h2,h3,h4{font-family:"Raleway",Arial,sans-serif;color:var(--ink)}
.wrap{width:1020px;margin:0 auto}
section,header,nav,footer{position:relative;overflow:hidden}
.accent{color:var(--blue)}
.btn{display:inline-block;background:var(--blue);color:var(--white);font-family:"Raleway",sans-serif;font-weight:700;font-size:12px;letter-spacing:.5px;padding:9px 18px;text-transform:uppercase}
.sec-title{text-align:center;font-size:32px;font-weight:800;text-transform:uppercase;letter-spacing:.5px}
.sec-title.light{color:var(--white)}
.center{text-align:center}

/* header */
.site-header{height:95px;background:var(--ink)}
.site-header .wrap{display:flex;align-items:center;justify-content:space-between;height:95px}
.office{color:#c9ced5;font-size:12px;line-height:1.7}
.office b{color:var(--white)}
.brand{display:flex;align-items:center;gap:10px;color:var(--white);font-family:"Raleway",sans-serif;font-weight:800;font-size:26px;letter-spacing:1px;text-transform:uppercase}
.brand-mark{width:34px;height:34px;background:var(--blue);border-radius:50%}
.account{display:flex;gap:18px;color:var(--white);font-size:12px;font-weight:700;text-transform:uppercase}
.main-nav{height:40px;background:var(--blue)}
.main-nav ul{list-style:none;display:flex;justify-content:center;height:40px}
.main-nav li{color:var(--white);font-size:12px;font-weight:600;text-transform:uppercase;padding:0 30px;line-height:40px}
.main-nav li.active{background:var(--blue-dark)}

/* hero */
.hero{height:470px;background:linear-gradient(90deg,#8b98a6 0%,#b9c3cd 40%,#e7ebef 70%,#cfd6dd 100%)}
.hero-photo{position:absolute;inset:0}
.hero-copy{position:absolute;left:90px;top:110px;width:520px}
.hero-copy h1{color:var(--white);font-size:31px;line-height:1.3;font-weight:700;margin-bottom:22px}

/* stats */
.stats{height:200px;background:var(--pale)}
.stats ul{list-style:none;display:flex;justify-content:space-between;width:1040px;margin:0 auto;position:relative;top:-45px}
.stats li{width:150px;text-align:center;font-family:"Raleway",sans-serif;font-weight:700;font-size:14px;color:var(--ink);line-height:1.35}
.stat-icon{width:104px;height:104px;border-radius:50%;background:var(--blue);border:5px solid var(--white);margin:0 auto 14px;display:flex;align-items:center;justify-content:center;box-shadow:0 2px 6px rgba(0,0,0,.15)}

/* incentives */
.incentives{height:470px;padding-top:34px}
.incentives h2{text-align:center;color:var(--blue);font-size:22px;font-weight:700;margin-bottom:34px}
.incentive-grid{display:flex;justify-content:space-between}
.incentive{width:230px;text-align:center}
.incentive h3{font-size:15px;font-weight:700;line-height:1.35;height:42px;margin-bottom:10px}
.incentive .thumb{height:140px;margin-bottom:10px}
.incentive p{font-size:12px;line-height:1.5;height:78px}
.incentive .price{color:var(--blue);font-weight:700}

/* distribution */
.distribution{height:400px;background:linear-gradient(180deg,#1a1e24,#2a3038);padding-top:62px}
.steps{display:flex;justify-content:space-between;margin-top:48px;position:relative}
.steps::before{content:"";position:absolute;left:120px;right:120px;top:45px;border-top:2px dashed #5c6570}
.step{width:220px;text-align:center;position:relative}
.step-icon{width:90px;height:90px;border-radius:50%;background:var(--blue);margin:0 auto 16px;display:flex;align-items:center;justify-content:center}
.step h3{color:var(--white);font-size:18px;margin-bottom:6px}
.step p{color:#b8bfc8;font-size:12px;line-height:1.5}

/* promotional material */
.material{height:480px;padding-top:56px}
.material h2{text-align:center;font-size:28px;font-weight:800;text-transform:uppercase;line-height:1.25}
.material-grid{display:flex;justify-content:space-between;margin:36px 0 26px}
.material-item{width:220px;text-align:center}
.material-item .thumb{height:120px;margin-bottom:10px}
.material-item h3{color:var(--blue);font-size:16px}
.body-copy p{font-size:12px;margin-bottom:10px}

/* protect */
.protect{height:450px;background:var(--pale);padding-top:60px}
.subhead{text-align:center;font-weight:700;color:var(--ink);font-size:14px;margin:24px 0 14px}
.protect .body-copy p,.sounds .body-copy p,.about .body-copy p{text-align:center}

/* sounds */
.sounds{height:480px;padding-top:60px}

/* service */
.service{height:290px;background:linear-gradient(180deg,#20252c,#343b45);padding-top:52px}
.service .subhead{color:var(--white);margin:20px 0 12px}
.service p{color:#c3c9d0;text-align:center;font-size:12px;margin-bottom:10px}

/* about / history */
.about{height:300px;padding-top:48px}
.history{height:240px;background:var(--pale);padding-top:48px}
.history p{text-align:center;font-size:12px;margin-bottom:10px}
.about .subhead{margin:18px 0 10px}
.rule{width:60px;height:3px;background:var(--blue);margin:10px auto 0}

/* testimonials */
.testimonials{height:340px;padding-top:48px}
.testimonials h2{text-align:center;font-size:30px;font-weight:700}
.quote{position:relative;margin:26px auto 0;width:860px;text-align:center;font-size:13px;font-style:italic}
.quote .mark{position:absolute;top:-20px;font-family:Georgia,serif;font-size:70px;color:#c9ced5;font-style:normal;line-height:1}
.quote .mark.open{left:-60px}.quote .mark.close{right:-60px}
.quote cite{display:block;font-style:normal;color:var(--blue);font-weight:700;font-family:"Raleway",sans-serif;font-size:18px;margin-top:14px}
.avatars{display:flex;justify-content:center;gap:26px;margin-top:16px}
.avatar{width:66px;height:66px;border-radius:50%;background:linear-gradient(135deg,#c8b6a6,#8e7a6b);border:3px solid var(--white);box-shadow:0 0 0 2px var(--line)}
.avatar.current{width:78px;height:78px;box-shadow:0 0 0 3px var(--blue)}

/* cta */
.cta{height:180px;background:var(--blue);padding-top:40px;text-align:center}
.cta h2{color:var(--white);font-size:25px;font-weight:700;line-height:1.35}
.btn.outline{background:transparent;border:2px solid var(--white);margin-top:16px}

/* brochure & clients */
.showcase{height:400px;padding-top:56px}
.showcase .wrap{display:flex;justify-content:space-between}
.showcase h2{font-size:25px;font-weight:800;text-transform:uppercase;margin-bottom:22px}
.brochure{width:460px}
.brochure-body{display:flex;gap:20px}
.brochure-body p{font-size:12px;width:190px}
.brochure .thumb{width:250px;height:170px}
.clients{width:490px}
.client-grid{display:grid;grid-template-columns:1fr 1fr;gap:16px}
.client{height:90px;border:1px solid var(--line);display:flex;align-items:center;justify-content:center;font-family:"Raleway",sans-serif;font-weight:800;font-size:20px;color:var(--ink)}

/* footer */
.site-footer{height:367px;background:var(--ink);padding-top:50px;color:#aeb5be}
.footer-cols{display:flex;justify-content:space-between}
.site-footer h4{color:var(--white);font-size:14px;text-transform:uppercase;margin-bottom:16px;letter-spacing:.5px}
.site-footer ul{list-style:none;font-size:12px;line-height:2}
.contact-line{display:flex;gap:10px;font-size:12px;margin-bottom:10px;line-height:1.5}
.contact-line svg{flex:none;margin-top:2px}
.form-field{width:230px;height:28px;background:var(--white);margin-bottom:8px}
.form-field.tall{height:56px}
.footer-brand{text-align:center;width:220px}
.footer-brand .brand{justify-content:center;font-size:20px;margin-bottom:16px}
.social{display:flex;justify-content:center;gap:10px}
.social span{width:28px;height:28px;border-radius:50%;background:var(--blue)}
.copyright{position:absolute;bottom:0;left:0;right:0;height:44px;line-height:44px;text-align:center;font-size:11px;border-top:1px solid #343a42}
</style>
</head>
<body>

<header class="site-header">
  <div class="wrap">
    <div class="office">
      <div>USA Office : <b>555-014-2236</b></div>
      <div>International : <b>1-800-555-0199</b></div>
    </div>
    <div class="brand"><span class="brand-mark"></span>BrightLane Promoworks</div>
    <div class="account"><span>Login</span><span>Signup</span></div>
  </div>
</header>

<nav class="main-nav">
  <ul>
    <li class="active">Home</li><li>Our Incentives</li><li>Samples</li><li>How It Works</li><li>Testimonials</li><li>FAQ</li><li>Contact</li>
  </ul>
</nav>

<section class="hero">
  <div class="hero-photo" role="img" aria-label="Business team smiling together around a laptop in a bright office"></div>
  <div class="hero-copy">
    <h1>Increase Leads &amp; Sales From Your Existing Marketing Efforts By Offering High Perceived Value Incentives To Your Customers!</h1>
    <span class="btn">Sign Up Risk Free For 30 Days</span>
  </div>
</section>

<section class="stats">
  <ul>
    <li><div class="stat-icon"><svg width="44" height="44" viewBox="0 0 44 44" fill="none" stroke="#fff" stroke-width="3"><path d="M6 38h32M10 30l9-9 7 6 12-14"/><path d="M31 13h7v7"/></svg></div>12 Years In Business</li>
    <li><div class="stat-icon"><svg width="48" height="40" viewBox="0 0 48 40" fill="#fff"><circle cx="24" cy="12" r="8"/><path d="M10 38c0-9 6-14 14-14s14 5 14 14z"/><circle cx="9" cy="15" r="5"/><circle cx="39" cy="15" r="5"/></svg></div>13,000+ Clients Enrolled</li>
    <li><div class="stat-icon"><svg width="40" height="44" viewBox="0 0 40 44" fill="none" stroke="#fff" stroke-width="3"><rect x="6" y="4" width="28" height="36"/><path d="M12 14h16M12 21h16M12 28h10"/></svg></div>1+ Million Certificates In Circulation</li>
    <li><div class="stat-icon"><svg width="44" height="44" viewBox="0 0 44 44" fill="none" stroke="#fff" stroke-width="3"><rect x="6" y="16" width="32" height="22"/><path d="M4 10h36v6H4zM22 10v28"/></svg></div>170,000+ Redemptions To Date</li>
    <li><div class="stat-icon"><svg width="40" height="44" viewBox="0 0 40 44" fill="none" stroke="#fff" stroke-width="3"><rect x="5" y="4" width="30" height="36"/><path d="M13 22l5 5 10-11"/></svg></div>A+ Business Rating</li>
    <li><div class="stat-icon"><svg width="44" height="44" viewBox="0 0 44 44" fill="none" stroke="#fff" stroke-width="3"><circle cx="22" cy="18" r="11"/><path d="M15 27l-4 13 11-5 11 5-4-13"/></svg></div>Licensed Seller Of Travel CST #4820117</li>
  </ul>
</section>

<section class="incentives">
  <div class="wrap">
    <h2>Create Promotional Giveaways Using Any Of These Incentives</h2>
    <div class="incentive-grid">
      <div class="incentive">
        <h3>Vacation Getaway Certificates</h3>
        <div class="thumb" role="img" aria-label="Tropical beach at sunset" style="background:linear-gradient(180deg,#e79a4b,#b44f6f 55%,#2b5f93)"></div>
        <p><b>Cove At Sunset</b><br>5-7 Nights Including Airfare<br>Up To <span class="price">$2000</span> Value<br>Your customers just pay taxes</p>
        <span class="btn">More Details</span>
      </div>
      <div class="incentive">
        <h3>Restaurant Gift Certificates</h3>
        <div class="thumb" role="img" aria-label="Plated restaurant dishes on a table" style="background:linear-gradient(135deg,#8a5a33,#c9a46b 50%,#5e7b3a)"></div>
        <p><span class="price">$300.00</span><br>(10 – $25 restaurant certificates)<br>Valid at thousands of eateries</p>
        <span class="btn">More Details</span>
      </div>
      <div class="incentive">
        <h3>Electronic Product Giveaways</h3>
        <div class="thumb" role="img" aria-label="Tablets, phones and cameras arranged together" style="background:linear-gradient(135deg,#3a4350,#8d98a6 55%,#d3d9df)"></div>
        <p>Tablets, Premium Earbuds, Smart Watches<br>Valued At <span class="price">$100-$150</span> Value</p>
        <span class="btn">More Details</span>
      </div>
      <div class="incentive">
        <h3>Gas Or Grocery Rewards</h3>
        <div class="thumb" role="img" aria-label="Fresh groceries and a fuel pump" style="background:linear-gradient(135deg,#d9d2c3,#b7c79a 55%,#e4e8ec)"></div>
        <p>Available in<br><span class="price">just $99/each</span></p>
        <span class="btn">More Details</span>
      </div>
    </div>
  </div>
</section>

<section class="distribution" role="img" aria-label="Dark photo backdrop of a busy office" >
  <div class="wrap">
    <h2 class="sec-title light">Easy Distribution Of <span class="accent">Incentives</span></h2>
    <div class="steps">
      <div class="step"><div class="step-icon"><svg width="40" height="40" viewBox="0 0 40 40" fill="none" stroke="#fff" stroke-width="3"><path d="M11 15V5h18v10M11 29H5V15h30v14h-6"/><rect x="11" y="23" width="18" height="12"/></svg></div><h3>Print</h3><p>Download PDF certificates to print and physically hand them out or mail them to your customers.</p></div>
      <div class="step"><div class="step-icon"><svg width="40" height="40" viewBox="0 0 40 40" fill="none" stroke="#fff" stroke-width="3"><rect x="4" y="9" width="32" height="22"/><path d="M4 9l16 13 16-13"/></svg></div><h3>E-Mail</h3><p>Email E-Certificates to your customers individually or in bulk with just one click.</p></div>
      <div class="step"><div class="step-icon"><svg width="40" height="40" viewBox="0 0 40 40" fill="none" stroke="#fff" stroke-width="3"><circle cx="20" cy="20" r="15"/><path d="M5 20h30M20 5c6 5 6 25 0 30M20 5c-6 5-6 25 0 30"/></svg></div><h3>Online Automation</h3><p>Add our web banners to your website. Your customers click on the banner to get their certificate.</p></div>
      <div class="step"><div class="step-icon"><svg width="40" height="40" viewBox="0 0 40 40" fill="none" stroke="#fff" stroke-width="3"><path d="M5 7h30v20H16l-8 7v-7H5z"/><path d="M12 15h16M12 20h10"/></svg></div><h3>Text Messaging</h3><p>Send your certificates through text messaging with just one click! (Coming Soon)</p></div>
    </div>
  </div>
</section>

<section class="material">
  <div class="wrap">
    <h2>Promotional Marketing Material To Help You<br><span class="accent">Promote The Incentives To Your Customers</span></h2>
    <div class="material-grid">
      <div class="material-item"><div class="thumb" role="img" aria-label="Vacation promotion poster" style="background:linear-gradient(135deg,#6ab0d8,#e9c98f)"></div><h3>Posters</h3></div>
      <div class="material-item"><div class="thumb" role="img" aria-label="Stack of printed promotional flyers" style="background:linear-gradient(135deg,#c84a3c,#f0b36a)"></div><h3>Flyers</h3></div>
      <div class="material-item"><div class="thumb" role="img" aria-label="Sample letter template pages" style="background:linear-gradient(135deg,#e5e8ec,#b9c2cc)"></div><h3>Letter Templates</h3></div>
      <div class="material-item"><div class="thumb" role="img" aria-label="Notebook with marketing tips" style="background:linear-gradient(135deg,#f1e6c6,#d9b45c)"></div><h3>Tips</h3></div>
    </div>
    <div class="body-copy center">
      <p>We help you by providing full color, professionally designed flyers and posters for each incentive that you can print at your local print shop or on your own office printing equipment.</p>
      <p>We also provide you with customer appreciation letter templates and sample tips and strategies to help you get the most from your promotional marketing campaigns.</p>
    </div>
  </div>
</section>

<section class="protect">
  <div class="wrap">
    <h2 class="sec-title">We Protect The Integrity Of <span class="accent">Your Promotions</span></h2>
    <p class="subhead">Separate Redemption Websites with Online Reservation Systems.</p>
    <div class="body-copy">
      <p>First and foremost we're a marketing company so we want to protect the integrity of your promotions. We do this by using separate redemption websites which keeps your customers from being confused about who issued their reward and keeps your brand front and center.</p>
      <p>Your customers will never know about BrightLane Promoworks unless they read the fine print, so your business receives the full credit and goodwill for every reward you give away.</p>
      <p>Our redemption process is very easy and user friendly. Most of your customers will redeem their certificates online and can track their reservations through our online reservation system, so there are no long hold times or missed calls.</p>
      <p>When your customers redeem a certificate they can always log back in to their account to check on the status of their offer at any time, day or night.</p>
    </div>
  </div>
</section>

<section class="sounds">
  <div class="wrap">
    <h2 class="sec-title">Sounds To Good To Be True?</h2>
    <p class="subhead">How Do We Do It?</p>
    <div class="body-copy">
      <p>First and foremost we're a marketing company so we want to protect the integrity of your promotions.</p>
      <p>We contract with the world's leading hotel chains and resorts and cruise lines to help them fill their otherwise empty rooms when they need it most. We help fill empty rooms which the properties turn into additional revenue from other parts of their property.</p>
      <p>What you have to understand is that hotels and resorts are known to have many expenses that are fixed, so an empty room earns them nothing while an occupied room brings in spending.</p>
      <p>So when the properties give out their rooms by partnering with us, they might miss out on the room fee up front, but they gain dining, spa and activity revenue from every guest who visits.</p>
      <p>They're also doing it for the same reason why you would be using these incentives: to introduce new repeat and referral business. They know that if their guests have a great stay, they will return and tell their friends.</p>
      <p>Since we contract with the largest travel companies in the industry, this ensures top quality rewards for your customers with absolutely no timeshare or sales presentations required, guaranteed.</p>
    </div>
  </div>
</section>

<section class="service" role="img" aria-label="Dark photo backdrop of a customer service agent with a headset">
  <div class="wrap">
    <h2 class="sec-title light">Top Level <span class="accent">Customer Service</span></h2>
    <p class="subhead">We answer our phones!</p>
    <p>We are easy to contact and we always answer our phone during business hours and are adding the ability to correspond through text messaging. We even have a 24 hour live answering service that takes our calls to ensure we never miss a call.</p>
    <p>Your customers are our top priority. We facilitate them all the way from redemption to fulfillment to ensure a seamless and easy experience.</p>
    <p>With our support ticket system, our 800 line, online contact forms and live chat, someone is always ready to help you or your customers get the most from their rewards.</p>
  </div>
</section>

<section class="about">
  <div class="wrap">
    <h2 class="sec-title">Who We Are</h2>
    <p class="subhead">About Us:</p>
    <div class="body-copy">
      <p>As a premier marketing company, BrightLane Promoworks proudly offers businesses and their customers a wide range of marketing incentives, including the best pricing available.</p>
      <p>We have revolutionized the travel incentive industry by introducing the first modern benefits organization. We are devoted to helping businesses generate better results from their advertising and promotions by providing high perceived value rewards at a low cost.</p>
      <p>Incentive marketing has been used for years as a powerful promotional tool but only affordable to the large corporations. Our incentives are now priced for businesses of every size, from single storefronts to national brands.</p>
      <p>Our promotions and quality customer service boost your business, building long-term relationships with loyal customers.</p>
    </div>
  </div>
</section>

<section class="history">
  <div class="wrap">
    <h2 class="sec-title">Our History</h2>
    <div class="rule"></div>
    <p style="margin-top:22px">We were created in 2005 and legally incorporated in 2006 in business for over 12 years.</p>
    <p>We've enrolled more than 13,000 businesses into our program who are responsible for distributing over one million certificates that resulted in over 170,000 redemptions.</p>
    <p>We are a licensed seller of travel registered with the state and we participate in the travel consumer restitution fund, which was created to protect consumers from dishonest travel companies.</p>
  </div>
</section>

<section class="testimonials">
  <div class="wrap">
    <h2>Client <span class="accent">Testimonials</span></h2>
    <blockquote class="quote">
      <span class="mark open">“</span>
      Our customers loved the vacation certificates and our referrals doubled within three months. The materials were ready to print, setup took minutes, and every redemption went smoothly. We now use these incentives in every campaign we run and recommend them to every owner we meet.
      <span class="mark close">”</span>
      <cite>Marcus</cite>
    </blockquote>
    <div class="avatars">
      <div class="avatar" role="img" aria-label="Client portrait"></div>
      <div class="avatar current" role="img" aria-label="Client portrait"></div>
      <div class="avatar" role="img" aria-label="Client portrait"></div>
    </div>
  </div>
</section>

<section class="cta">
  <h2>Know Any Businesses That Could Benefit Using<br>Incentives To Bring In More Customers?</h2>
  <span class="btn outline">Click Here</span>
</section>

<section class="showcase">
  <div class="wrap">
    <div class="brochure">
      <h2>View Our Online <span class="accent">Brochure</span></h2>
      <div class="brochure-body">
        <p>Take a quick tour of every incentive we offer, with pricing, redemption details and sample marketing material, all in one easy online brochure you can share with your team.</p>
        <div class="thumb" role="img" aria-label="Open brochure showing a tropical resort" style="background:linear-gradient(135deg,#2f7fbf,#8fd0e6 55%,#f0e3bf)"></div>
      </div>
      <span class="btn" style="margin-top:18px">Click Here</span>
    </div>
    <div class="clients">
      <h2>Our <span class="accent">Clients</span></h2>
      <div class="client-grid">
        <div class="client">Northgate Realty</div>
        <div class="client">ValueVault</div>
        <div class="client">Meridian Motors</div>
        <div class="client">Skyline TV</div>
      </div>
    </div>
  </div>
</section>

<footer class="site-footer">
  <div class="wrap footer-cols">
    <div>
      <h4>Quick Links</h4>
      <ul><li>Home</li><li>Our Incentives</li><li>Samples</li><li>How It Works</li><li>Testimonials</li><li>FAQ</li><li>Contact Us</li></ul>
    </div>
    <div>
      <h4>Contact Details</h4>
      <div class="contact-line"><svg width="12" height="14" viewBox="0 0 12 14" fill="#1679c6"><path d="M6 0a5 5 0 0 0-5 5c0 4 5 9 5 9s5-5 5-9a5 5 0 0 0-5-5z"/></svg><span><b style="color:#fff">www.brightlanepromoworks.biz</b><br>1840 Harbor Way, Suite 210<br>Bayview, CA 90210</span></div>
      <div class="contact-line"><svg width="12" height="14" viewBox="0 0 12 14" fill="#1679c6"><path d="M2 0h3l1 3-2 2c1 2 2 3 4 4l2-2 3 1v3c0 1-1 2-2 2C5 13 0 8 0 2 0 1 1 0 2 0z"/></svg><span>555-014-2236<br>1-800-555-0199</span></div>
      <div class="contact-line"><svg width="12" height="12" viewBox="0 0 12 12" fill="none" stroke="#1679c6" stroke-width="1.6"><circle cx="6" cy="6" r="5"/><path d="M6 3v3l2 1"/></svg><span>Hours: Mon-Fri 9am-4pm PST<br>Sat-Sun Closed</span></div>
    </div>
    <div>
      <h4>Contact Now</h4>
      <div class="form-field"></div>
      <div class="form-field"></div>
      <div class="form-field tall"></div>
      <span class="btn">Submit</span>
    </div>
    <div class="footer-brand">
      <div class="brand"><span class="brand-mark"></span>BrightLane</div>
      <div class="social"><span></span><span></span><span></span><span></span></div>
    </div>
  </div>
  <div class="copyright">Copyright 2017 © BrightLane Promoworks. All rights reserved.</div>
</footer>

</body>
</html>
```